Business Card Design Project

We need a business card design for a new company based in New York called "Marble Fox's". We do major installations of energy saving devices primarily LED lighting in large facilities. We would like a double sided card with our contact info on one side with our logo (to be designed) and on the other side the services we provide. We would like a heavy weight glossy card using the colors green and white. The final design should communicate environmental soundness and our market is very upscale corporations.
We would like our logo to illustrate LED lighting and we were thinking if we could get a stock picture of the Corliss Vane Building lit up on July 4th with red, white and blue LED lighting. The alternative would be anything that connotes environmentally proper thinking. It could be either a picture or a design.

```html
<!DOCTYPE html>
<html lang="en">
<head>
<meta charset="utf-8">
<title>Marble Fox's — Business Cards</title>
<link href="https://fonts.googleapis.com/css2?family=Quicksand:wght@500;600;700&display=swap" rel="stylesheet">
<style>
  :root {
    --stage: #262626;
    --card-light: #1e1f1f;
    --card-dark: #090a0a;
    --green: #8cc63f;
    --green-deep: #5f9a25;
    --band: rgba(70, 120, 30, 0.55);
    --white: #f2f2f2;
    --divider: rgba(255, 255, 255, 0.08);
  }
  * { box-sizing: border-box; margin: 0; padding: 0; }
  html, body { width: 1200px; height: 900px; overflow: hidden; background: var(--stage); }
  body { position: relative; font-family: "Quicksand", sans-serif; }

  .card {
    position: absolute;
    width: 502px;
    height: 274px;
    overflow: hidden;
    background: radial-gradient(ellipse at 45% 25%, var(--card-light), var(--card-dark) 80%);
    box-shadow: 0 4px 14px rgba(0, 0, 0, 0.6);
  }
  .col-front { left: 77px; }
  .col-back { left: 627px; }
  .row-1 { top: 19px; }
  .row-2 { top: 312px; }
  .row-3 { top: 605px; }

  /* front */
  .brand {
    position: absolute;
    left: 0; right: 0;
    display: flex;
    flex-direction: column;
    align-items: center;
    gap: 14px;
    z-index: 1;
  }
  .brand-dot {
    width: 74px; height: 74px;
    border-radius: 50%;
    background: var(--green);
  }
  .brand-name {
    font-weight: 700;
    font-size: 44px;
    line-height: 1;
    color: var(--green);
    letter-spacing: 0.5px;
  }
  .row-1 .brand, .row-2 .brand { top: 58px; }
  .row-3 .brand { top: 60px; }
  .band {
    position: absolute;
    left: 0; right: 0;
    background: linear-gradient(to bottom, rgba(70,120,30,0.35), var(--band), rgba(70,120,30,0.35));
  }
  .band-foot { top: 250px; height: 24px; }
  .band-mid { top: 212px; height: 36px; z-index: 0; }

  /* back */
  .holder {
    position: absolute;
    color: var(--green);
    font-weight: 500;
    font-size: 22px;
    line-height: 1;
    padding: 6px 28px 6px 20px;
    background: linear-gradient(to right, rgba(95,154,37,0.45), rgba(95,154,37,0.25) 75%, rgba(95,154,37,0));
  }
  .holder.plain { background: none; padding-left: 40px; font-size: 19px; }

  .contacts { position: absolute; list-style: none; }
  .contacts li {
    height: 21px;
    display: flex;
    align-items: center;
    gap: 14px;
    color: var(--white);
    font-size: 11px;
    font-weight: 500;
    white-space: nowrap;
  }
  .contacts.align-right li { justify-content: flex-end; }
  .contacts.align-left li { gap: 26px; }
  .contacts .icon { width: 14px; height: 14px; fill: var(--white); flex: none; }
  .contacts.align-right .icon { margin-left: 10px; }

  .divider {
    position: absolute;
    width: 2px;
    background: linear-gradient(to bottom, rgba(255,255,255,0), var(--divider) 30%, var(--divider) 70%, rgba(255,255,255,0));
  }
  .tagline { position: absolute; color: var(--green); font-weight: 500; }
  .tagline.block { font-size: 13.5px; line-height: 16px; text-align: center; width: 190px; }
  .tagline.line { font-size: 10px; white-space: nowrap; }

  .emblem {
    position: absolute;
    width: 136px; height: 136px;
    border-radius: 50%;
    background: radial-gradient(circle at 40% 35%, var(--green), var(--green-deep));
  }
</style>
</head>
<body>
<svg width="0" height="0" style="position:absolute" aria-hidden="true">
  <defs>
    <symbol id="icon-phone" viewBox="0 0 16 16"><path d="M2 6c0-2 2-3 6-3s6 1 6 3v1h-3V5.5H5V7H2z"/><rect x="3" y="8" width="10" height="6" rx="1"/></symbol>
    <symbol id="icon-pin" viewBox="0 0 16 16"><path d="M8 1a5 5 0 0 0-5 5c0 4 5 9 5 9s5-5 5-9a5 5 0 0 0-5-5zm0 7a2 2 0 1 1 0-4 2 2 0 0 1 0 4z"/></symbol>
    <symbol id="icon-mail" viewBox="0 0 16 16"><path d="M1 4h14v9H1z"/><path d="M1 4l7 5 7-5" fill="none" stroke="#111" stroke-width="1.3"/></symbol>
    <symbol id="icon-globe" viewBox="0 0 16 16"><path fill="none" stroke="#f2f2f2" stroke-width="1.2" d="M8 1.5a6.5 6.5 0 1 0 0 13 6.5 6.5 0 0 0 0-13zM1.5 8h13M8 1.5c-3 3.5-3 9.5 0 13M8 1.5c3 3.5 3 9.5 0 13M3 4.5h10M3 11.5h10"/></symbol>
  </defs>
</svg>

<!-- Row 1 -->
<section class="card col-front row-1">
  <div class="brand"><span class="brand-dot"></span><span class="brand-name">Marble Fox's</span></div>
</section>
<section class="card col-back row-1">
  <p class="holder plain" style="left:0; top:37px;">John Doe</p>
  <ul class="contacts align-right" style="right:255px; top:98px;">
    <li>212 406 7781<svg class="icon"><use href="#icon-phone"/></svg></li>
    <li>4410 Alder Row Brookhaven, NY 10001<svg class="icon"><use href="#icon-pin"/></svg></li>
    <li>hello@marblefoxs.com<svg class="icon"><use href="#icon-mail"/></svg></li>
    <li>www.marblefoxs.com<svg class="icon"><use href="#icon-globe"/></svg></li>
  </ul>
  <span class="divider" style="left:246px; top:70px; height:180px;"></span>
  <p class="tagline block" style="left:296px; top:114px;">Install energy saving devices primarily LED lighting for large facilities</p>
</section>

<!-- Row 2 -->
<section class="card col-front row-2">
  <div class="brand"><span class="brand-dot"></span><span class="brand-name">Marble Fox's</span></div>
  <span class="band band-foot"></span>
</section>
<section class="card col-back row-2">
  <p class="holder" style="left:0; top:40px;">John Doe</p>
  <ul class="contacts align-right" style="right:228px; top:95px;">
    <li>212 406 7781<svg class="icon"><use href="#icon-phone"/></svg></li>
    <li>4410 Alder Row Brookhaven, NY 10001<svg class="icon"><use href="#icon-pin"/></svg></li>
    <li>hello@marblefoxs.com<svg class="icon"><use href="#icon-mail"/></svg></li>
    <li>www.marblefoxs.com<svg class="icon"><use href="#icon-globe"/></svg></li>
  </ul>
  <span class="divider" style="left:254px; top:80px; height:170px;"></span>
  <span class="emblem" style="left:340px; top:119px;"></span>
  <p class="tagline line" style="left:16px; top:252px;">Install energy saving devices primarily LED lighting for large facilities</p>
</section>

<!-- Row 3 -->
<section class="card col-front row-3">
  <span class="band band-mid"></span>
  <div class="brand"><span class="brand-dot"></span><span class="brand-name">Marble Fox's</span></div>
</section>
<section class="card col-back row-3">
  <p class="holder" style="left:0; top:122px;">John Doe</p>
  <ul class="contacts align-left" style="left:228px; top:95px;">
    <li><svg class="icon"><use href="#icon-phone"/></svg>212 406 7781</li>
    <li><svg class="icon"><use href="#icon-pin"/></svg>4410 Alder Row Brookhaven, NY 10001</li>
    <li><svg class="icon"><use href="#icon-mail"/></svg>hello@marblefoxs.com</li>
    <li><svg class="icon"><use href="#icon-globe"/></svg>www.marblefoxs.com</li>
  </ul>
  <span class="divider" style="left:251px; top:80px; height:120px;"></span>
  <p class="tagline line" style="right:6px; top:255px;">Install energy saving devices primarily LED lighting for large facilities</p>
</section>
</body>
</html>
```